Folder outside surface for Marlowe Eye Studios

Hello :
Attached, please see the images and logo that are meant for a 9x12 inch folder. I need a 300dpi file (png, jpeg, and vector) that fits the diagram from a printing company.

```html
<!DOCTYPE html>
<html lang="en">
<head>
<meta charset="utf-8">
<title>Marlowe Eye Studios – Folder Outside Surface</title>
<link href="https://fonts.googleapis.com/css2?family=Montserrat:wght@500;800&display=swap" rel="stylesheet">
<style>
  :root {
    --backdrop: #8f8f8f;
    --navy-top: #0b2a8c;
    --navy-mid: #06165c;
    --navy-deep: #020833;
    --band-blue: #0a2f8a;
    --accent-orange: #e0621c;
    --accent-teal: #13808a;
    --text-white: #ffffff;
  }
  * { margin: 0; padding: 0; box-sizing: border-box; }
  html, body {
    width: 1200px;
    height: 1200px;
    overflow: hidden;
    background: var(--backdrop);
  }
  .canvas {
    position: relative;
    width: 1200px;
    height: 1200px;
    display: flex;
    align-items: center;
    justify-content: center;
  }
  .folder-cover {
    position: relative;
    width: 810px;
    height: 1080px;
    overflow: hidden;
    background: linear-gradient(180deg, var(--navy-top) 0%, var(--navy-mid) 45%, var(--navy-deep) 72%);
    box-shadow: 0 10px 30px rgba(0,0,0,0.25);
  }
  .tech-pattern {
    position: absolute;
    top: -60px;
    right: -40px;
    width: 520px;
    height: 520px;
    border-radius: 50%;
    background: radial-gradient(circle, rgba(40,80,190,0.35) 0%, rgba(30,70,180,0.18) 45%, rgba(20,50,150,0) 70%);
  }
  .brand-block {
    position: absolute;
    top: 330px;
    left: 0;
    width: 100%;
    text-align: center;
    color: var(--text-white);
    font-family: "Montserrat", sans-serif;
  }
  .brand-name {
    display: inline-flex;
    align-items: center;
    gap: 18px;
    font-weight: 800;
    font-size: 52px;
    line-height: 1.05;
    letter-spacing: 1px;
    text-transform: uppercase;
    color: var(--text-white);
  }
  .brand-dot {
    width: 26px;
    height: 26px;
    border-radius: 50%;
    background: var(--accent-orange);
    flex: none;
  }
  .brand-rule {
    width: 190px;
    height: 2px;
    margin: 34px auto 26px;
    background: var(--accent-teal);
  }
  .tagline {
    font-weight: 500;
    font-size: 19px;
    letter-spacing: 5px;
    line-height: 1.6;
    text-transform: uppercase;
    color: var(--text-white);
  }
  .bottom-sweep {
    position: absolute;
    left: 0;
    bottom: 0;
    width: 810px;
    height: 420px;
  }
</style>
</head>
<body>
  <main class="canvas">
    <section class="folder-cover">
      <div class="tech-pattern" role="img" aria-label="Faint technical circular eye-scan pattern in soft blue"></div>

      <div class="brand-block">
        <div class="brand-name"><span class="brand-dot"></span>Marlowe<br>Eye Studios</div>
        <div class="brand-rule"></div>
        <p class="tagline">Trusted Care<br>Guided by Science</p>
      </div>

      <svg class="bottom-sweep" viewBox="0 0 810 420" aria-hidden="true">
        <path d="M0 170 Q 380 300 810 150 L 810 420 L 0 420 Z" fill="var(--band-blue)"/>
        <path d="M0 250 Q 400 360 810 230 L 810 420 L 0 420 Z" fill="var(--navy-mid)"/>
        <path d="M0 160 Q 200 228 405 232" fill="none" stroke="var(--accent-orange)" stroke-width="6"/>
        <path d="M405 232 Q 620 236 810 140" fill="none" stroke="var(--accent-teal)" stroke-width="6"/>
      </svg>
    </section>
  </main>
</body>
</html>
```